依頼詳細
新春キャンペーンに向けてのチラシの作成をお願いします。
暁光時報の折り込みチラシ用を想定しています。

<入会特典>
パーソナルジム通常入会金22,000円→0円
事務手数料→0円
プロテイン3kg分プレゼント

基本メニューは下記になります。

スタンダードコースご利用料金
262,000円(税込)16回×50分
(上下ウェア・タオル・ドリンク・プロテイン)

以前他のパーソナルトレーニングジム会員の方 乗り換え特典で更にお得
224,000円(税込)16回×50分
(上下ウェア・タオル・ドリンク・プロテイン)

スタンダードコース終了後 更にお得な継続コースをご用意。

継続プラン
116,000円(税込)8回×50分
224,000円(税込)16回×50分
324,000円(税込)24回×50分
(上下ウェア・タオル・ドリンク・プロテイン)
記載項目
K VORTA 浦和店
〒338–0472
埼玉県さいたま市浦和区若葉台7-15八幡ビル4階
☎︎048-592-7716
サイズ
B4
ページ数
両面
希望イメージ
シンプル 複雑
単色 カラフル
暗い 明るい
日常 高級
遊び心 厳粛
未来的 伝統的
女性的 男性的
希望する色
赤系、黄・オレンジ系、無彩色系、金色
納品ファイル
• イラストレーター形式 (.ai)
補足説明
①添付のビフォーアフター写真、及び下記体組計データを掲載して
『2ヶ月で人はここまで変わる』というメッセージを打ち出したいです。

<女性>
お腹周り91cm→68cm
腕周り33cm→28cm
太腿周り59cm→52cm
体重63.05kg→51.95kg
体脂肪率40%→28%

<男性>
お腹周り98cm→77cm
腕周り36cm→35cm
太腿周り59cm→55cm
体重81.50kg→64.90kg
体脂肪率30%→13%

②チラシ裏面に、在籍トレーナーや店舗設備の写真を掲載して
店舗の雰囲気が伝わるように表現をして頂きたいです。
スペースの関係上難しい場合は、店舗設備の写真は不要でも問題ありません。

③添付ロゴを黒背景のオレンジ文字に変換して掲載をお願い致します。
添付のスタッフ写真には『ケイヴォルタ浦和店マネージャー倉持』と記載頂けますと幸いです。

<PRポイント>
■年間200名のお客様を担当
■8ヶ月で最大40kgのダイエット指導実績
■目標達成率98.7%を誇る指導力
■自ら3ヶ月で15kgのダイエットに成功
■フィットスターアジア2019さいたま大会グランプリ受賞

デザインや色合い、写真の加工や情報の表現について、こちらの理想通りに仕上げて頂きました。
また、細部にまで細かい配慮をして頂き非常に助かりました。ありがとうございます!!

ご提案頂きましたランサーの方々、お忙しい中データ作成して頂きまして誠にありがとうございます。
大変恐縮ながら、今回は当選者の方のご提案でお願いする運びとなりました。またご機会がございましたら何卒よろしくお願い申し上げます。

```html
<!DOCTYPE html>
<html lang="ja">
<head>
<meta charset="utf-8">
<title>K VORTA 新春キャンペーン</title>
<link rel="stylesheet" href="https://fonts.googleapis.com/css2?family=Noto+Sans+JP:wght@500;700;900&family=Noto+Serif+JP:wght@600;900&display=swap">
<style>
:root{
  --ink:#120c08;
  --ink-2:#1e140e;
  --ember:#c8321a;
  --flame:#f07a18;
  --gold:#ffc21a;
  --sun:#ffe24a;
  --cream:#fff6e6;
  --white:#ffffff;
  --panel:#f3efe9;
  --man:#f07a18;
  --woman:#e0306e;
}
*{margin:0;padding:0;box-sizing:border-box}
html,body{width:852px;height:1200px;overflow:hidden;background:var(--ink)}
.flyer{position:relative;width:852px;height:1200px;overflow:hidden;background:var(--ink);font-family:"Noto Sans JP",sans-serif;color:var(--white)}
.burst{position:absolute;inset:0}
.brand{position:absolute;top:18px;right:26px;display:flex;align-items:center;gap:8px}
.brand__dot{width:30px;height:30px;border-radius:50%;background:var(--flame)}
.brand__name{font-weight:900;font-size:26px;letter-spacing:1px;color:var(--flame)}
.headline{position:absolute;left:0;right:0;top:52px;text-align:center;font-weight:900;line-height:1.06;letter-spacing:2px}
.headline span{display:block;background:linear-gradient(180deg,var(--sun) 0%,var(--gold) 40%,var(--flame) 100%);-webkit-background-clip:text;background-clip:text;color:transparent;filter:drop-shadow(0 4px 0 #3a0d04) drop-shadow(0 0 6px rgba(0,0,0,.7))}
.headline__l1{font-size:104px;padding-left:20px}
.headline__l2{font-size:112px}
.photo{position:absolute;border-radius:4px}
.photo--man-before{left:34px;top:380px;width:190px;height:380px;background:linear-gradient(180deg,#b98a6a,#6e4a36 70%,#2c2522)}
.photo--man-after{left:205px;top:350px;width:230px;height:500px;background:linear-gradient(180deg,#c79674,#7a4f36 65%,#2b2b33)}
.photo--woman-after{left:440px;top:350px;width:220px;height:500px;background:linear-gradient(180deg,#d3a685,#8e6149 50%,#1b1b1b)}
.photo--woman-before{left:660px;top:380px;width:170px;height:380px;background:linear-gradient(180deg,#d0a584,#96705a 60%,#2a2a2a)}
.arrow{position:absolute;top:520px}
.arrow--left{left:158px}
.arrow--right{left:594px}
.loss{position:absolute;top:712px;font-family:"Noto Serif JP",serif;font-weight:900;font-style:italic;font-size:92px;color:var(--white);text-shadow:0 3px 8px rgba(0,0,0,.8);letter-spacing:-2px}
.loss--man{left:70px}
.loss--woman{left:520px}
.stats{position:absolute;top:856px;width:382px;height:228px;background:var(--ink-2);border:2px solid var(--flame);display:flex;align-items:center;padding:0 14px;gap:14px}
.stats--man{left:40px}
.stats--woman{left:438px;border-color:var(--woman)}
.stats__tag{flex:none;width:92px;height:92px;border-radius:50%;border:3px solid var(--man);display:flex;align-items:center;justify-content:center;font-weight:700;font-size:20px;color:var(--man);letter-spacing:1px}
.stats--woman .stats__tag{border-color:var(--woman);color:var(--woman);font-size:17px}
.stats__list{list-style:none;flex:1}
.stats__row{display:flex;align-items:center;font-size:16px;line-height:39px;border-bottom:1px solid rgba(255,255,255,.15);white-space:nowrap}
.stats__row:last-child{border-bottom:none}
.stats__row b{font-weight:500;width:118px;color:#d8d0c6}
.stats__row i{font-style:normal;color:var(--gold);margin:0 8px;font-size:13px}
.stats__row strong{font-weight:900;font-size:24px;color:var(--white)}
.offer{position:absolute;left:0;right:0;top:1098px;height:102px;background:var(--panel);display:flex;align-items:center;padding:0 16px;gap:12px;color:var(--ink)}
.offer__badge{flex:none;width:132px;height:80px;background:var(--ember);color:var(--white);display:flex;flex-direction:column;align-items:center;justify-content:center;gap:4px;font-weight:900;line-height:1.2;white-space:nowrap}
.offer__badge small{font-size:14px;color:var(--gold);letter-spacing:0}
.offer__badge span{font-size:22px;letter-spacing:1px}
.offer__item{flex:1;display:flex;align-items:center;justify-content:center;gap:8px;border-left:1px solid #c9bfb2;height:76px}
.offer__badge + .offer__item{border-left:none}
.offer__label{display:flex;flex-direction:column;align-items:center;font-weight:700;font-size:16px;line-height:1.35;white-space:nowrap}
.offer__was{font-size:11px;font-weight:500;background:#fff;border:1px solid #999;padding:0 5px;text-decoration:line-through;margin-top:3px}
.offer__value{font-family:"Noto Sans JP",sans-serif;font-weight:900;font-size:56px;color:var(--ember);line-height:1;white-space:nowrap}
.offer__value small{font-size:26px}
</style>
</head>
<body>
<main class="flyer">
  <svg class="burst" viewBox="0 0 852 1200" width="852" height="1200" aria-hidden="true">
    <defs>
      <radialGradient id="glow" cx="426" cy="520" r="520" gradientUnits="userSpaceOnUse">
        <stop offset="0" stop-color="#6e1a0c"/>
        <stop offset=".6" stop-color="#2a0f08"/>
        <stop offset="1" stop-color="#120c08"/>
      </radialGradient>
      <linearGradient id="beam" x1="0" y1="0" x2="1" y2="1">
        <stop offset="0" stop-color="#f07a18"/>
        <stop offset="1" stop-color="#b8230f"/>
      </linearGradient>
    </defs>
    <rect width="852" height="1200" fill="url(#glow)"/>
    <g opacity=".85">
      <polygon points="40,0 150,0 500,560 390,620" fill="url(#beam)"/>
      <polygon points="812,0 702,0 352,560 462,620" fill="url(#beam)"/>
      <polygon points="0,820 0,700 426,520 460,600" fill="#8f1e0c"/>
      <polygon points="852,820 852,700 426,520 392,600" fill="#8f1e0c"/>
    </g>
    <circle cx="426" cy="560" r="170" fill="none" stroke="#c8321a" stroke-width="18" opacity=".7"/>
  </svg>

  <div class="brand"><span class="brand__dot"></span><span class="brand__name">K VORTA</span></div>

  <h1 class="headline">
    <span class="headline__l1">2ヶ月で人は</span>
    <span class="headline__l2">ここまで変わる</span>
  </h1>

  <div class="photo photo--man-before" role="img" aria-label="男性会員のトレーニング前の全身写真"></div>
  <div class="photo photo--woman-before" role="img" aria-label="女性会員のトレーニング前の全身写真"></div>
  <div class="photo photo--man-after" role="img" aria-label="男性会員の2ヶ月後の全身写真"></div>
  <div class="photo photo--woman-after" role="img" aria-label="女性会員の2ヶ月後の全身写真"></div>

  <svg class="arrow arrow--left" width="90" height="70" viewBox="0 0 90 70" aria-hidden="true">
    <polygon points="0,18 50,18 50,0 90,35 50,70 50,52 0,52" fill="#ffc21a"/>
  </svg>
  <svg class="arrow arrow--right" width="90" height="70" viewBox="0 0 90 70" aria-hidden="true">
    <polygon points="90,18 40,18 40,0 0,35 40,70 40,52 90,52" fill="#ffc21a"/>
  </svg>

  <p class="loss loss--man">-14kg</p>
  <p class="loss loss--woman">-12kg</p>

  <section class="stats stats--man">
    <div class="stats__tag">MAN</div>
    <ul class="stats__list">
      <li class="stats__row"><b>お腹周り 98cm</b><i>▶</i><strong>77cm</strong></li>
      <li class="stats__row"><b>腕周り 36cm</b><i>▶</i><strong>35cm</strong></li>
      <li class="stats__row"><b>太腿周り 59cm</b><i>▶</i><strong>55cm</strong></li>
      <li class="stats__row"><b>体重 81.50kg</b><i>▶</i><strong>64.90kg</strong></li>
      <li class="stats__row"><b>体脂肪率 30%</b><i>▶</i><strong>13%</strong></li>
    </ul>
  </section>

  <section class="stats stats--woman">
    <div class="stats__tag">WOMAN</div>
    <ul class="stats__list">
      <li class="stats__row"><b>お腹周り 91cm</b><i>▶</i><strong>68cm</strong></li>
      <li class="stats__row"><b>腕周り 33cm</b><i>▶</i><strong>28cm</strong></li>
      <li class="stats__row"><b>太腿周り 59cm</b><i>▶</i><strong>52cm</strong></li>
      <li class="stats__row"><b>体重 63.05kg</b><i>▶</i><strong>51.95kg</strong></li>
      <li class="stats__row"><b>体脂肪率 40%</b><i>▶</i><strong>28%</strong></li>
    </ul>
  </section>

  <section class="offer">
    <div class="offer__badge"><small>新春キャンペーン</small><span>入会特典</span></div>
    <div class="offer__item">
      <div class="offer__label">パーソナルジム<br>通常入会金<span class="offer__was">通常22,000円</span></div>
      <div class="offer__value">0<small>円</small></div>
    </div>
    <div class="offer__item">
      <div class="offer__label">事務手数料<span class="offer__was">通常10,000円</span></div>
      <div class="offer__value">0<small>円</small></div>
    </div>
    <div class="offer__item">
      <div class="offer__label">プロテイン<br>プレゼント</div>
      <div class="offer__value">3<small>kg</small></div>
    </div>
  </section>
</main>
</body>
</html>
```